Analytics/BI tech start-up seeks sharp, creative, simple, secret agent type logo & theme

"Quarry 7 Technologies" seeks a logo design/color scheme template for NYC based tech start-up of software engineers, solutions architects, and data/BI analysts. We develop reporting solutions and analytics platforms for small-medium sized businesses. We code for database, cloud, and web/mobile apps.<br/><br/>Some *very basic, limited* sketches are attached to show ideas we've had. We need a logo and color scheme that may be used for business cards, paper letterhead and envelopes, and web pages to be published at "www.quarry7.dev".<br/><br/>We like the black/red, red/white, blue/black, white/black contrasts as a stating point, and prefer black background business cards, but open to anything if it feels like a good match. We are relying on the projects submitted here to take care of the creativity part of our image, which we work on logistics to launching our start-up. Something that could also be easily translated into black/white, grayscale would be appreciated as well. while log is important, we also need an icon that may be used as an app thumbnail. For font, we prefer all caps.<br/><br/>Business: Quarry 7 Technologies<br/>Slogan: If. Else. Us. / If -> Else -> Us / If - Else - Us / etc.<br/>Website: www.quarry.dev<br/>Icon: [Q7] , only as a starting point<br/>Theme Ideas: Sleek, futuristic, secret agent-like tech, simple, bold color contrasts, software code related<br/><br/>Feel free to reach out to jvorenko@mailbarn.example as a contact for any questions or follow up. We look forward to seeing amazing ideas!
Updates

We would like to provide the opportunity for as many different submissions as possible.

Target Market(s)

Small business owners, entrepreneurs, financial/tech companies, freelance engineers, people in need of IT assistance to elevate business

Industry/Entity Type

It Company

Contact Information for Business Card

Individual Info: Name, Position, Phone Number 1, Phone Number 2 (optional), Fax Number, email Address.
Company Info: Name, logo, icon (optional), web site, slogan

Font styles to use
Sans Serif
Other font styles liked:
• Similar to Biome Light All Caps, Hollow Meridian type style

Requirements
Must have
• Pronounced 1 in the logo, either in the word Section or not. Bold color contrast, one side with only logo or icon, possible web address too. Other side with all individual info plus logo, and/or icon and web address. If using uploaded files as a base, center the C more between the E and T, it is too closer to the T as is.
Nice to have
• Bolder font possibly, more square edged at ends of letters but still with minor curved corners. Icon suggested as a starting point is “[Q7]” and instead of a slogan, use "Data - Cloud - Web - Software" and the dividers don't necessary have to be hyphens.
Should not have
• Open to all creative ideas, try anything. Please come up with different logos than are in the attached files, they are meant as a starting point.

```html
<!DOCTYPE html>
<html lang="en">
<head>
<meta charset="UTF-8">
<title>Quarry 7 Technologies – Business Card</title>
<link href="https://fonts.googleapis.com/css2?family=Oswald:wght@700&family=Work+Sans:wght@300;400&display=swap" rel="stylesheet">
<style>
  :root {
    --stage: #1b1b1b;
    --card: #242424;
    --cyan: #4ef2f5;
    --ink: #f2f2f2;
    --mark: #9a9a9a;
  }
  * { margin: 0; padding: 0; box-sizing: border-box; }
  html, body { width: 1200px; height: 900px; overflow: hidden; }
  body {
    background: var(--stage);
    font-family: "Work Sans", Arial, sans-serif;
    position: relative;
  }
  .card {
    position: absolute;
    left: 290px;
    width: 620px;
    height: 354px;
    background: var(--card);
    color: var(--ink);
  }
  .card--front { top: 70px; }
  .card--back { top: 470px; }

  .front-mark {
    position: absolute;
    top: 112px; left: 0; right: 0;
    text-align: center;
    font-weight: 300;
    font-size: 72px;
    letter-spacing: 6px;
    color: var(--mark);
    text-transform: uppercase;
    line-height: 1;
    white-space: nowrap;
  }
  .front-url {
    position: absolute;
    bottom: 34px; left: 0; right: 0;
    text-align: center;
    font-size: 19px;
    letter-spacing: 2px;
  }

  .brand {
    position: absolute;
    top: 40px; left: 0; right: 0;
    text-align: center;
    color: var(--cyan);
    font-weight: 300;
    text-transform: uppercase;
    line-height: 1.05;
    white-space: nowrap;
  }
  .brand__name { font-size: 62px; letter-spacing: 5px; display: block; }
  .brand__sub { font-size: 30px; letter-spacing: 3px; display: block; }

  .person {
    position: absolute;
    top: 190px; left: 20px;
    width: 278px;
    text-align: right;
    white-space: nowrap;
  }
  .person__name {
    font-family: "Oswald", Arial, sans-serif;
    font-weight: 700;
    font-size: 36px;
    color: var(--cyan);
    text-transform: uppercase;
    letter-spacing: 1px;
    line-height: 1.1;
  }
  .person__role { font-size: 17px; letter-spacing: 1.5px; margin-top: 2px; }

  .divider {
    position: absolute;
    top: 196px; left: 316px;
    width: 2px; height: 76px;
    background: var(--cyan);
  }

  .contact {
    position: absolute;
    top: 196px; left: 338px;
    list-style: none;
    font-size: 17px;
    letter-spacing: 1.5px;
    white-space: nowrap;
  }
  .contact li { display: flex; align-items: center; gap: 12px; height: 26px; }
  .contact svg { width: 14px; height: 14px; flex: none; }

  .address {
    position: absolute;
    bottom: 30px; left: 0; right: 0;
    text-align: center;
    font-size: 18px;
    letter-spacing: 2px;
  }
</style>
</head>
<body>

<section class="card card--front">
  <div class="front-mark">Quarry 7</div>
  <p class="front-url">www.quarry.dev</p>
</section>

<section class="card card--back">
  <h1 class="brand">
    <span class="brand__name">Quarry 7</span>
    <span class="brand__sub">Technologies</span>
  </h1>

  <div class="person">
    <p class="person__name">Dara Kessling</p>
    <p class="person__role">Director</p>
  </div>

  <div class="divider"></div>

  <ul class="contact">
    <li>
      <svg viewBox="0 0 14 14" aria-hidden="true"><path d="M3 1l2.5 3-1.4 1.6c.8 1.7 2.1 3 3.8 3.8L9.5 8 13 10.5l-1.2 2.3C6.5 13 1 7.5 1.2 2.2z" fill="none" stroke="var(--cyan)" stroke-width="1.2"/></svg>
      +41700555014
    </li>
    <li>
      <svg viewBox="0 0 14 14" aria-hidden="true"><rect x="1" y="3" width="12" height="8" fill="none" stroke="var(--cyan)" stroke-width="1.2"/><path d="M1 3l6 5 6-5" fill="none" stroke="var(--cyan)" stroke-width="1.2"/></svg>
      info@quarry7.dev
    </li>
    <li>
      <svg viewBox="0 0 14 14" aria-hidden="true"><circle cx="7" cy="7" r="6" fill="none" stroke="var(--cyan)" stroke-width="1.1"/><ellipse cx="7" cy="7" rx="2.6" ry="6" fill="none" stroke="var(--cyan)" stroke-width="1"/><path d="M1 7h12M2 4h10M2 10h10" stroke="var(--cyan)" stroke-width="0.9"/></svg>
      www.quarry7.dev
    </li>
  </ul>

  <p class="address">2218 Foundry Lane Harlow, 98000</p>
</section>

</body>
</html>
```